Business Card for Trivelo, a french tech company

Tech company
New technologies
Serious design
Dark theme

User info :
Name: Florian GASTIER
Position: Co-Founder & CEO
Tel: (+33) 6 52 84 26 07
Email: florian@trivelo.example
Website: www.trivelo.example
Address: 17 rue des Tanneurs 69001 LYON

```html
<!DOCTYPE html>
<html lang="fr">
<head>
<meta charset="utf-8">
<title>Trivelo — Business Card</title>
<link rel="stylesheet" href="https://fonts.googleapis.com/css2?family=Roboto:wght@400;500;700&display=swap">
<style>
  :root {
    --backdrop: #ababab;
    --card-deep: #0c1649;
    --card-mid: #0b2c62;
    --card-light: #0a5682;
    --ink: #ffffff;
    --shadow: rgba(0, 0, 0, 0.35);
  }
  * { margin: 0; padding: 0; box-sizing: border-box; }
  html, body {
    width: 1200px;
    height: 1000px;
    overflow: hidden;
    background: var(--backdrop);
    font-family: "Roboto", Arial, sans-serif;
    color: var(--ink);
  }
  .card {
    position: absolute;
    width: 613px;
    height: 352px;
    border-radius: 24px;
    background: linear-gradient(90deg, var(--card-deep) 0%, var(--card-mid) 45%, var(--card-light) 100%);
    box-shadow: 0 18px 40px var(--shadow);
    overflow: hidden;
  }
  .card--front { left: 293px; top: 118px; }
  .card--back  { left: 294px; top: 530px; }

  .wordmark {
    position: absolute;
    font-weight: 700;
    letter-spacing: 0.02em;
    line-height: 1;
    white-space: nowrap;
  }
  .card--front .wordmark { left: 52px; top: 168px; font-size: 58px; }
  .card--back .wordmark  { left: 319px; top: 72px; font-size: 39px; }

  .holder {
    position: absolute;
    right: 354px;
    top: 163px;
    text-align: right;
  }
  .holder__name { font-weight: 700; font-size: 17px; line-height: 22px; }
  .holder__role { font-weight: 400; font-size: 18px; line-height: 22px; }

  .contact {
    position: absolute;
    left: 319px;
    font-size: 14px;
    line-height: 17px;
  }
  .contact--address { top: 163px; }
  .contact--reach   { top: 230px; }
</style>
</head>
<body>
  <section class="card card--front" aria-label="Front of the card">
    <div class="wordmark">TRIVELO</div>
  </section>

  <section class="card card--back" aria-label="Back of the card">
    <div class="holder">
      <p class="holder__name">Florian GASTIER</p>
      <p class="holder__role">Co-Founder &amp; CEO</p>
    </div>
    <div class="wordmark">TRIVELO</div>
    <address class="contact contact--address" style="font-style:normal">
      17 rue des Tanneurs<br>69001 LYON
    </address>
    <p class="contact contact--reach">
      (+33) 6 52 84 26 07<br>florian@trivelo.example<br>www.trivelo.example
    </p>
  </section>
</body>
</html>
```